Harbor Ridge Elementary School Letterhead

We would like a letterhead that includes our school mascot (Flicker the Falcon), school address, and phone number. We want something with personality and a little fun. Our school colors are navy blue, green (like the flag in our graphic), and gray. We included an example of a letterhead we like the feel of (on the fun side). The example is the image titled "sample." We are the Harbor Ridge Falcons.
Harbor Ridge Elementary
Address: 418 Marlow Fern, Irvine, CA 92781
Phone: (949) 555-0174
harborridge.oksd.example
Target Market(s)
Elementary School Families

```html
<!DOCTYPE html>
<html lang="en">
<head>
<meta charset="utf-8">
<title>Harbor Ridge Elementary School Letterhead</title>
<link rel="stylesheet" href="https://fonts.googleapis.com/css2?family=Oswald:wght@500&family=Poppins:wght@400;500;600&display=swap">
<style>
  :root {
    --navy: #1d2d5c;
    --school-blue: #2b3b8f;
    --ink: #222530;
    --muted: #8a8d99;
    --icon-light: #8e9ed0;
    --icon-mid: #5a70c0;
    --icon-deep: #2f4aa8;
    --mascot-gray: #9a9ca3;
    --backdrop: #ffffff;
  }
  * { box-sizing: border-box; margin: 0; padding: 0; }
  html, body { width: 1021px; height: 1200px; overflow: hidden; background: var(--backdrop); }
  body { font-family: "Poppins", sans-serif; color: var(--ink); }

  .letterhead {
    position: absolute; left: 85px; top: 0;
    width: 851px; height: 1200px; background: #fff;
  }
  .side-band { position: absolute; left: 0; top: 0; width: 46px; height: 1200px; background: var(--navy); }
  .side-foot {
    position: absolute; left: 0; top: 1052px; width: 82px; height: 148px;
    background: var(--navy); border-top-right-radius: 14px; overflow: hidden;
  }
  .side-foot .cap { position: absolute; left: 46px; top: 0; width: 36px; height: 8px; background: var(--icon-light); border-top-right-radius: 14px; }

  .masthead {
    position: absolute; left: 250px; top: 60px; width: 500px; height: 60px;
    display: flex; align-items: center; justify-content: center; gap: 14px;
  }
  .masthead .dot { width: 22px; height: 22px; border-radius: 50%; background: var(--school-blue); }
  .masthead .name {
    font-family: "Oswald", sans-serif; font-weight: 500; font-size: 40px;
    color: var(--school-blue); text-transform: uppercase; letter-spacing: 1px;
  }

  .mascot-art {
    position: absolute; left: 55px; top: 207px; width: 158px; height: 134px;
    border-radius: 50% 50% 40% 40%;
    background: radial-gradient(circle at 45% 40%, #c7c9ce, var(--mascot-gray) 70%, #7d8088);
  }

  .school-block { position: absolute; left: 67px; top: 350px; }
  .school-block .school-name {
    font-family: "Oswald", sans-serif; font-weight: 500; color: var(--school-blue);
    text-transform: uppercase; line-height: 1.1;
  }
  .school-name .line-1 { display: block; font-size: 24px; }
  .school-name .line-2 { display: block; font-size: 18px; margin-top: 2px; letter-spacing: 0.4px; }
  .school-block .address { margin-top: 22px; font-size: 14.5px; line-height: 21px; }

  .recipient { position: absolute; left: 261px; top: 206px; font-size: 13.5px; line-height: 19px; }
  .recipient .to { font-size: 13px; }
  .recipient .rcpt-name { font-size: 17px; font-weight: 600; color: var(--school-blue); letter-spacing: 0.8px; margin: 1px 0 3px; }
  .recipient b { font-weight: 600; }

  .date { position: absolute; right: 38px; top: 266px; font-size: 13.5px; }
  .date b { color: var(--school-blue); font-weight: 600; }

  .letter-body { position: absolute; left: 253px; top: 356px; width: 560px; }
  .letter-body p {
    font-size: 11.6px; line-height: 18.4px; text-align: justify; margin-bottom: 18.4px;
  }
  .letter-body .soft { color: var(--muted); }

  .signature-art {
    position: absolute; left: 258px; top: 918px; width: 168px; height: 30px;
    background: linear-gradient(90deg, #e4e5ea, #f3f3f6);
  }
  .sign-rule { position: absolute; left: 254px; top: 956px; width: 177px; height: 2px; background: var(--ink); }
  .designation { position: absolute; left: 263px; top: 966px; font-size: 11.5px; font-weight: 600; letter-spacing: 1px; }

  .contact { position: absolute; left: 46px; top: 1060px; }
  .contact li { list-style: none; display: flex; align-items: center; height: 34px; }
  .contact .icon {
    width: 36px; height: 34px; display: flex; align-items: center; justify-content: center;
  }
  .contact li:nth-child(1) .icon { background: var(--icon-light); }
  .contact li:nth-child(2) .icon { background: var(--icon-mid); }
  .contact li:nth-child(3) .icon { background: var(--icon-deep); }
  .contact .value { margin-left: 8px; font-size: 13.5px; }
</style>
</head>
<body>
<main class="letterhead">
  <div class="side-band"></div>
  <div class="side-foot"><span class="cap"></span></div>

  <header class="masthead">
    <span class="dot"></span>
    <span class="name">Harbor Ridge</span>
  </header>

  <div class="mascot-art" role="img" aria-label="Illustration of Flicker the Falcon, the school mascot, waving a green flag"></div>

  <section class="school-block">
    <h1 class="school-name"><span class="line-1">Harbor Ridge</span><span class="line-2">Elementary School</span></h1>
    <p class="address">418 Marlow Fern, Irvine,<br>CA 92781</p>
  </section>

  <section class="recipient">
    <p class="to">To</p>
    <p class="rcpt-name">Nora Whitfield</p>
    <p>CEO, BRIGHTLANE CO</p>
    <p><b>W:</b> www.brightlane.example</p>
  </section>

  <p class="date"><b>Date:</b> 24-03-2018</p>

  <article class="letter-body">
    <p class="soft">Lorem ipsum dolor sit amet, consectetur adipiscing elit. Pellentesque dictum, ante non ullamcorp er convallis, nunc quam blandit metus, ac mollis eros felis a orci. Donec congue, mauris ut pulvinar lobortis, dolor massa feugiat nisi, at tincidunt metus leo vel elit. Proin facilisis semper lobortis. Vivamus augue purus, cursus quis urna non, accumsan pellentesque est. Nulla in iaculis magna, quis aliqu et ex. Cras efficitur metus eget purus euismod facilisis. Proin non metus tincidunt, auctor ipsum a, tempor mi.</p>
    <p>Nulla egestas vulputate risus, ut vestibulum diam commodo id. Mauris ornare libero eu erat portt itor ultrices. Proin sed lectus scelerisque ligula bibendum sagittis ac nec leo. Donec ac accumsan diam, et lobortis mauris.</p>
    <p>Nulla congue volutpat nisl ac lobortis. Integer dignissim interdum libero, quis feugiat velit pretium at. Phasellus sit amet libero rutrum, feugiat odio et, tempus purus. Cras ultricies, leo at fringilla solli cit udin, leo sapien placerat enim, a rutrum lorem enim ut tortor. Phasellus magna ante, cong ue maximus egestas sit amet, venenatis scelerisque felis.</p>
    <p class="soft">Nulla congue volutpat nisl ac lobortis. Integer dignissim interdum libero, quis feugiat velit pretium at. Phasellus sit amet libero rutrum, feugiat odio et, tempus purus. Cras ultricies, leo at fringilla solli cit udin, leo sapien placerat enim, a rutrum lorem enim ut tortor. Phasellus magna ante, cong ue maximus egestas sit amet, venenatis scelerisque felis.</p>
    <p class="soft">Curabitur vitae urna volutpat, varius velit vehicula, fermentum magna. In maximus metus nunc, nec aliquet justo commodo eget. Nullam rhoncus vehicula gravida. Maecenas non sem at erat lacinia con vallis. Aliquam at lobortis erat.</p>
    <p class="soft">Nulla congue volutpat nisl ac lobortis. Integer dignissim interdum libero, quis feugiat velit pretium at. Phasellus sit amet libero rutrum, feugiat odio et, tempus purus. Cras ultricies, leo at fringilla solli cit udin, leo sapien placerat enim, a rutrum lorem enim ut tortor. Phasellus magna ante, cong ue maximus egestas sit amet, venenatis scelerisque felis</p>
  </article>

  <div class="signature-art" role="img" aria-label="Space for the handwritten signature"></div>
  <div class="sign-rule"></div>
  <p class="designation">DESIGNATION PLACE HERE</p>

  <ul class="contact">
    <li>
      <span class="icon"><svg width="13" height="13" viewBox="0 0 24 24"><path fill="#fff" d="M6.6 10.8a15.1 15.1 0 0 0 6.6 6.6l2.2-2.2c.3-.3.7-.4 1-.2 1.1.4 2.3.6 3.6.6.6 0 1 .4 1 1V20c0 .6-.4 1-1 1A17 17 0 0 1 3 4c0-.6.4-1 1-1h3.5c.6 0 1 .4 1 1 0 1.3.2 2.5.6 3.6.1.3 0 .7-.2 1z"/></svg></span>
      <span class="value">(949) 555-0174</span>
    </li>
    <li>
      <span class="icon"><svg width="13" height="11" viewBox="0 0 24 18"><path fill="#fff" d="M0 2 12 10 24 2V16c0 1.1-.9 2-2 2H2c-1.1 0-2-.9-2-2zM1 0h22L12 7z"/></svg></span>
      <span class="value">info@harborridge.oksd.example</span>
    </li>
    <li>
      <span class="icon"><svg width="13" height="13" viewBox="0 0 24 24"><g fill="none" stroke="#fff" stroke-width="2"><circle cx="12" cy="12" r="10"/><ellipse cx="12" cy="12" rx="4.5" ry="10"/><path d="M2 12h20M4 7h16M4 17h16"/></g></svg></span>
      <span class="value">www.harborridge.oksd.example</span>
    </li>
  </ul>
</main>
</body>
</html>
```